Website for Bramblewood Quarry Advisors

Please design a website that initially contains four or five pages. This work is for a newly formed consulting company, Bramblewood Quarry Advisors, that provides training and individual coaching to help business professionals and lawyers write more effectively and efficiently.

We work in a professional and conservative industry. The website should be simple, crisp, and clean.

I have attached a document that describes the four initial pages for the site: 1) a landing page, 2) a webpage that includes the pictures and bios of our two consultants, 3) a webpage that describes our services, and 4) a webpage that will contain a form that visitors can use to submit questions to us.

I also included the following files:
a. a powerpoint slide with our consultants' pictures and bios; and
b. our recently designed logo (jpg and png files).

Thank you!

```html
<!DOCTYPE html>
<html lang="en">
<head>
<meta charset="UTF-8">
<title>Bramblewood Quarry Advisors</title>
<link href="https://fonts.googleapis.com/css2?family=Lato:wght@300;400;700;900&display=swap" rel="stylesheet">
<style>
:root{
  --blue:#2e57a6;
  --blue-dark:#284a8c;
  --navy:#344c81;
  --ink:#4a4f5a;
  --muted:#7d838e;
  --line:#d9dde3;
  --white:#ffffff;
  --hero-a:#eef1f4;
  --hero-b:#dfe4ea;
}
*{box-sizing:border-box;margin:0;padding:0}
html,body{width:1200px;height:2216px;overflow:hidden}
body{font-family:'Lato',sans-serif;color:var(--ink);background:var(--white);position:relative}

.site-nav{height:46px;display:flex;align-items:center;justify-content:space-between;padding:0 44px 0 40px;background:var(--white);position:relative;z-index:2}
.brand{display:flex;align-items:center;gap:8px;font-size:13px;font-weight:700;color:var(--blue-dark)}
.brand-mark{width:10px;height:10px;background:var(--blue)}
.nav-links{display:flex;gap:26px;list-style:none;font-size:12px;font-weight:700;color:var(--blue-dark)}

.hero{position:relative;height:420px;padding:40px 150px 0;text-align:center}
.hero-photo{position:absolute;inset:0;background:linear-gradient(160deg,var(--hero-a) 0%,#f6f7f9 45%,var(--hero-b) 100%)}
.hero-content{position:relative}
.hero h1{font-size:50px;font-weight:700;color:var(--blue);letter-spacing:-.5px;margin-bottom:26px}
.hero p{font-size:14.5px;line-height:1.75;color:#555b66}

.section-bar{width:46px;height:5px;background:var(--blue);margin:0 auto 14px}
.section-title{font-size:42px;font-weight:700;color:var(--blue-dark);text-align:center}

.consultants{height:720px;padding:56px 90px 0;background:var(--white)}
.consultant-grid{display:grid;grid-template-columns:1fr 1fr;gap:50px;margin-top:40px}
.consultant{text-align:center}
.portrait{width:128px;height:128px;border-radius:50%;margin:0 auto 16px;background:radial-gradient(circle at 50% 40%,#c9a98e,#8c7868)}
.portrait.second{background:radial-gradient(circle at 50% 40%,#9a7560,#5b4a44)}
.consultant h3{font-size:20px;font-weight:700;color:#2d3340;margin-bottom:22px}
.consultant p{font-size:14px;line-height:1.85;color:var(--muted);text-align:left}

.services{position:relative;height:420px;padding:20px 90px 0}
.services-photo{position:absolute;inset:0;background:linear-gradient(180deg,#ffffff 0%,#eef0f3 40%,#e9ecef 100%)}
.services-content{position:relative}
.service-grid{display:grid;grid-template-columns:repeat(4,1fr);gap:40px;margin-top:50px}
.service-icon{width:30px;height:30px;margin-bottom:10px;stroke:#3a3f4a;fill:none;stroke-width:1.6}
.service h4{font-size:14px;font-weight:700;color:#2d3340;line-height:1.35;margin-bottom:14px;min-height:38px}
.service p{font-size:12.5px;line-height:1.7;color:var(--muted);margin-bottom:22px}
.btn-small{display:inline-block;font-size:10px;color:var(--blue);border:1px solid var(--blue);border-radius:3px;padding:5px 16px;background:var(--white)}

.contact{position:absolute;left:0;right:0;top:1606px;bottom:0;background:var(--navy);color:var(--white);padding:56px 0 0}
.contact .section-bar{background:var(--white)}
.contact .section-title{color:var(--white)}
.contact-form{display:grid;grid-template-columns:1fr 1fr;gap:0 200px;width:660px;margin:52px auto 0}
.field{font-size:15px;font-weight:700;padding-bottom:18px;border-bottom:1px solid rgba(255,255,255,.55);margin-bottom:40px;width:230px}
.submit-row{grid-column:2;margin-top:-6px}
.btn-submit{display:inline-block;background:#4a73c8;color:var(--white);font-size:13px;font-weight:700;padding:8px 28px;border-radius:3px}
.copyright{text-align:center;font-size:16px;font-weight:700;margin-top:60px}
</style>
</head>
<body>
<header class="site-nav">
  <div class="brand"><span class="brand-mark"></span>Bramblewood Quarry Advisors</div>
  <ul class="nav-links"><li>Home</li><li>About Us</li><li>Services</li><li>Contact Us</li></ul>
</header>

<section class="hero">
  <div class="hero-photo" role="img" aria-label="Faded background photo of a person writing at a laptop"></div>
  <div class="hero-content">
    <h1>Bramblewood Quarry Advisors</h1>
    <p>Bramblewood Quarry Advisors helps business professionals and lawyers write with clarity, precision and confidence. Our training programs and one-on-one coaching sessions focus on practical techniques that shorten drafting time, sharpen arguments and make every document easier to read. Whether you are preparing a client memo, a contract, a brief or a board report, we work alongside you to build habits that last. Clear writing saves time, reduces risk and strengthens the trust of the people you serve.</p>
  </div>
</section>

<section class="consultants">
  <div class="section-bar"></div>
  <h2 class="section-title">Our Consultants</h2>
  <div class="consultant-grid">
    <article class="consultant">
      <div class="portrait" role="img" aria-label="Portrait photo of consultant Maren Ashcroft"></div>
      <h3>Maren Ashcroft</h3>
      <p>Maren Ashcroft spent fifteen years as a litigator before turning her attention to teaching. She has drafted appellate briefs, negotiated complex agreements and supervised junior associates across several practice areas. Her workshops show lawyers how to organize their thinking before they write, how to cut needless words and how to present a persuasive argument in plain language. Maren has led sessions for law firms, corporate legal departments and bar associations, and she coaches individual writers who want steady, measurable progress. She holds a law degree and a master's degree in English, and she believes that good writing is a skill anyone can learn with practice and honest feedback.</p>
    </article>
    <article class="consultant">
      <div class="portrait second" role="img" aria-label="Portrait photo of consultant Dorian Welles"></div>
      <h3>Dorian Welles</h3>
      <p>Dorian Welles has worked as an editor, a communications director and a business writing instructor for more than two decades. He helps executives, managers and analysts turn dense material into reports, proposals and emails that readers understand on the first pass. His approach is practical: start with the reader, state the main point early and support it with clear structure. Dorian designs training programs tailored to each organization and follows up with individual coaching so that new habits take hold. Clients value his patient style, his sharp eye for detail and his ability to make writing feel less like a chore and more like a tool for getting work done.</p>
    </article>
  </div>
</section>

<section class="services">
  <div class="services-photo" role="img" aria-label="Faded background photo of a professional at a desk"></div>
  <div class="services-content">
    <div class="section-bar"></div>
    <h2 class="section-title">Our Services</h2>
    <div class="service-grid">
      <article class="service">
        <svg class="service-icon" viewBox="0 0 30 30"><circle cx="10" cy="10" r="4"/><circle cx="21" cy="10" r="4"/><path d="M3 25c0-5 3-8 7-8s7 3 7 8M14 25c0-5 3-8 7-8s7 3 7 8"/></svg>
        <h4>Training for business professionals</h4>
        <p>Group sessions that teach structure, clarity and concise style for reports, memos and everyday business correspondence.</p>
        <span class="btn-small">Learn more</span>
      </article>
      <article class="service">
        <svg class="service-icon" viewBox="0 0 30 30"><path d="M5 25l3-9 14-13 6 6-14 13z"/><path d="M8 16l6 6"/></svg>
        <h4>Coaching for lawyers and legal staff</h4>
        <p>Private coaching that reviews your own drafts and builds lasting habits through focused feedback and practice.</p>
        <span class="btn-small">Learn more</span>
      </article>
      <article class="service">
        <svg class="service-icon" viewBox="0 0 30 30"><path d="M7 3h12l5 5v19H7z"/><path d="M11 12h9M11 17h9M11 22h6"/></svg>
        <h4>Editing support for important documents</h4>
        <p>Guidance on briefs, contracts and letters so that legal documents stay precise, readable and persuasive.</p>
        <span class="btn-small">Learn more</span>
      </article>
      <article class="service">
        <svg class="service-icon" viewBox="0 0 30 30"><path d="M4 6h22v14H13l-6 5v-5H4z"/></svg>
        <h4>Workshops for teams</h4>
        <p>Custom programs for teams that share standards, templates and a common approach to writing.</p>
        <span class="btn-small">Learn more</span>
      </article>
    </div>
  </div>
</section>

<section class="contact">
  <div class="section-bar"></div>
  <h2 class="section-title">Contact Us</h2>
  <div class="contact-form">
    <div>
      <div class="field">Company Name</div>
      <div class="field">Contact Name</div>
      <div class="field">Contact Phone Number</div>
      <div class="field">Email Address</div>
    </div>
    <div>
      <div class="field">Physical Address</div>
      <div class="field">Open field</div>
    </div>
  </div>
  <div class="contact-form" style="margin-top:-80px">
    <div></div>
    <div class="submit-row"><span class="btn-submit">Submit</span></div>
  </div>
  <p class="copyright">Bramblewood Quarry Advisors Copyright 2024</p>
</section>
</body>
</html>
```